Cups in Quiet Bloom webdesign + shopvantix implementation

Hi there!
We are a brand new small company located in central Europe, specializing in handmade coffee and tea mugs - please check www.cupsinquietbloom.example

We are looking for a complete redesign, something easy, nothing complicated.

1. web desing (smooth and easy - homepage,product detail page, etc...)
2. html/css
3. shopvantix platform implementation

Industry/Entity Type

It Company

```html
<!DOCTYPE html>
<html lang="en">
<head>
<meta charset="utf-8">
<title>Cups in Quiet Bloom — Handmade Mugs</title>
<link rel="stylesheet" href="https://fonts.googleapis.com/css2?family=Varela+Round&family=Nunito:wght@700;800;900&display=swap">
<style>
  :root {
    --brown-dark: #5c3d22;
    --brown-band: #6b4426;
    --tan: #c2a27a;
    --tan-light: #f0e2cb;
    --header-bg: #f3f2f0;
    --page-bg: #ffffff;
    --photo-top: #6b6866;
    --photo-mid: #b9735c;
    --photo-base: #cdb89c;
  }
  * { box-sizing: border-box; margin: 0; padding: 0; }
  html, body { width: 1200px; height: 824px; overflow: hidden; background: var(--page-bg); }
  body { position: relative; font-family: "Nunito", "Varela Round", sans-serif; color: var(--brown-dark); }

  .site-header { position: absolute; left: 0; top: 0; width: 1200px; height: 188px; background: var(--header-bg); }
  .header-band { position: absolute; left: 0; top: 188px; width: 1200px; height: 10px; background: var(--brown-band); }

  .nav-item {
    position: absolute; transform: translateX(-50%); text-align: center;
    font-family: "Varela Round", sans-serif; font-size: 11.5px; line-height: 12px;
    text-transform: uppercase; color: var(--brown-dark); text-decoration: none; white-space: nowrap;
  }
  .nav-item.is-active { color: var(--tan); font-weight: 700; }

  .brand { position: absolute; left: 600px; top: 30px; transform: translateX(-50%); text-align: center; }
  .brand-dot { width: 46px; height: 46px; border-radius: 50%; background: var(--brown-band); margin: 0 auto 16px; }
  .brand-name { font-family: "Varela Round", sans-serif; font-size: 36px; color: var(--brown-dark); white-space: nowrap; }

  .intro { position: absolute; left: 0; top: 212px; width: 1200px; text-align: center; }
  .intro-lines { font-weight: 800; font-size: 24.5px; line-height: 27px; text-transform: uppercase; color: var(--tan); letter-spacing: 0.5px; }
  .intro-motto { margin-top: 10px; font-weight: 900; font-size: 43px; line-height: 50px; text-transform: uppercase; color: var(--brown-dark); letter-spacing: 1px; }

  .featured-title { position: absolute; left: 142px; top: 456px; font-weight: 800; font-size: 18.5px; text-transform: uppercase; color: var(--brown-dark); }
  .featured-title small { font-size: 12.5px; color: var(--tan); }

  .product-grid { position: absolute; left: 142px; top: 486px; width: 918px; display: grid; grid-template-columns: repeat(5, 165px); column-gap: 23px; row-gap: 0; }
  .product { width: 165px; height: 214px; text-align: center; }
  .product-photo { width: 165px; height: 109px; background: linear-gradient(180deg, var(--photo-top) 0%, var(--photo-mid) 55%, var(--photo-base) 100%); }
  .product-name { height: 30px; margin-top: 12px; display: flex; align-items: center; justify-content: center; font-family: "Varela Round", sans-serif; font-size: 11.5px; line-height: 13px; text-transform: uppercase; color: var(--brown-dark); }
  .product-price { font-weight: 800; font-size: 18px; line-height: 22px; color: var(--tan); }
  .add-to-cart {
    display: inline-flex; align-items: center; gap: 5px; margin-top: 3px; width: 124px; height: 26px; justify-content: center;
    background: linear-gradient(180deg, #f7ecd9, var(--tan-light)); border: 1px solid var(--brown-dark); border-radius: 4px;
    font-family: "Varela Round", sans-serif; font-size: 11.5px; text-transform: uppercase; color: var(--brown-dark);
  }
</style>
</head>
<body>
  <header class="site-header">
    <a class="nav-item is-active" style="left:176px;top:81px">Home<br>page</a>
    <a class="nav-item" style="left:271px;top:87px">Categories</a>
    <a class="nav-item" style="left:365px;top:81px">New<br>arrivals</a>
    <a class="nav-item" style="left:836px;top:81px">About<br>our mugs</a>
    <a class="nav-item" style="left:931px;top:87px">My account</a>
    <a class="nav-item" style="left:1023px;top:87px">Contact us</a>
    <div class="brand">
      <div class="brand-dot"></div>
      <div class="brand-name">Cups in Quiet Bloom</div>
    </div>
  </header>
  <div class="header-band"></div>

  <section class="intro">
    <p class="intro-lines">Hey coffee lovers!<br>Looking for a unique coffee mug?<br>We offer beautiful handmade coffee mugs and tea cups<br>born in the heart of Europe.<br>Beautiful design,<br>precise execution and piece of a heart.</p>
    <p class="intro-motto">Relax and “Mug the moment”!</p>
  </section>

  <h2 class="featured-title">Featured products <small>(1–20 of 20):</small></h2>

  <main class="product-grid">
    <article class="product"><div class="product-photo" role="img" aria-label="Terracotta mug painted with red hearts"></div><p class="product-name">Coffee mug with hearts</p><p class="product-price">$30.00</p><span class="add-to-cart"><svg width="20" height="14" viewBox="0 0 20 14"><rect x="1" y="1" width="14" height="12" rx="2" fill="#5c3d22"/><path d="M15 4h3v6h-3" fill="none" stroke="#5c3d22" stroke-width="2"/><path d="M8 3v8M4 7h8" stroke="#f0e2cb" stroke-width="2"/></svg>Add to cart</span></article>
    <article class="product"><div class="product-photo" role="img" aria-label="Mug with painted daisies, empty decor"></div><p class="product-name">Coffee mug with daisies<br>(empty decor)</p><p class="product-price">$30.00</p><span class="add-to-cart"><svg width="20" height="14" viewBox="0 0 20 14"><rect x="1" y="1" width="14" height="12" rx="2" fill="#5c3d22"/><path d="M15 4h3v6h-3" fill="none" stroke="#5c3d22" stroke-width="2"/><path d="M8 3v8M4 7h8" stroke="#f0e2cb" stroke-width="2"/></svg>Add to cart</span></article>
    <article class="product"><div class="product-photo" role="img" aria-label="Mug with painted daisies, filled decor"></div><p class="product-name">Coffee mug with daisies<br>(filled decor)</p><p class="product-price">$30.00</p><span class="add-to-cart"><svg width="20" height="14" viewBox="0 0 20 14"><rect x="1" y="1" width="14" height="12" rx="2" fill="#5c3d22"/><path d="M15 4h3v6h-3" fill="none" stroke="#5c3d22" stroke-width="2"/><path d="M8 3v8M4 7h8" stroke="#f0e2cb" stroke-width="2"/></svg>Add to cart</span></article>
    <article class="product"><div class="product-photo" role="img" aria-label="Mug with painted daisies, empty decor"></div><p class="product-name">Coffee mug with daisies<br>(empty decor)</p><p class="product-price">$30.00</p><span class="add-to-cart"><svg width="20" height="14" viewBox="0 0 20 14"><rect x="1" y="1" width="14" height="12" rx="2" fill="#5c3d22"/><path d="M15 4h3v6h-3" fill="none" stroke="#5c3d22" stroke-width="2"/><path d="M8 3v8M4 7h8" stroke="#f0e2cb" stroke-width="2"/></svg>Add to cart</span></article>
    <article class="product"><div class="product-photo" role="img" aria-label="Wide cup with painted daisies"></div><p class="product-name">Coffee mug with daisies<br>(empty decor)</p><p class="product-price">$30.00</p><span class="add-to-cart"><svg width="20" height="14" viewBox="0 0 20 14"><rect x="1" y="1" width="14" height="12" rx="2" fill="#5c3d22"/><path d="M15 4h3v6h-3" fill="none" stroke="#5c3d22" stroke-width="2"/><path d="M8 3v8M4 7h8" stroke="#f0e2cb" stroke-width="2"/></svg>Add to cart</span></article>

    <article class="product"><div class="product-photo" role="img" aria-label="Terracotta mug painted with red hearts"></div></article>
    <article class="product"><div class="product-photo" role="img" aria-label="Mug with painted daisies, empty decor"></div></article>
    <article class="product"><div class="product-photo" role="img" aria-label="Mug with painted daisies, filled decor"></div></article>
    <article class="product"><div class="product-photo" role="img" aria-label="Mug with painted daisies, empty decor"></div></article>
    <article class="product"><div class="product-photo" role="img" aria-label="Wide cup with painted daisies"></div></article>
  </main>
</body>
</html>
```